Flyer Design

I will be hosting an event at Penrith's open workroom. Here is a link to their page http://www.theopenworkroom.com.au/events-and-workshops/whats-on-penrith/. I have attached the details of my course from their website below. I hope this is of some valuable assistance.

Florist and lover of all things gorgeous, Molly Brandt from Molly Brandt Flowers will be running this beautiful and fun workshop. Come along to learn how to make your very own floral crown. All you need to bring are some closed in shoes, an apron and an open mind ready for creativity!

Teens & adults welcome

Date 1: Saturday 11 April 2015
Time 1: 11:00-2:00pm

Date 2: Thursday 23 April 2015
Time 2: 6:00-9:00pm

Cost: $90 per person (includes materials provided – see list below)
Place: The Open Workroom, Unit 3, 17 Holloway Street Penrith
RSVP: Molly via email mollybrandtflowers@postvale.com or phone 0431 507 962

Materials provided:
• Florist scissors
• Parafilm
• Wire
• Flowers
• light snacks & refreshments

```html
<!DOCTYPE html>
<html lang="en">
<head>
<meta charset="utf-8">
<title>Floral Crowns Workshop</title>
<link rel="stylesheet" href="https://fonts.googleapis.com/css2?family=Great+Vibes&family=Open+Sans:ital,wght@0,600;0,700;0,800;1,700&family=PT+Sans+Narrow&display=swap">
<style>
  :root {
    --pink-header: #f7c0d8;
    --magenta: #d1367a;
    --ring: #c8457f;
    --lime: #c9d86a;
    --lime-deep: #a8bd3c;
    --lime-pale: #e3e8a4;
    --band: rgba(176, 140, 120, 0.72);
    --band-low: rgba(200, 170, 140, 0.55);
    --ink: #1e1e1e;
    --rose-photo-a: #e8d2a8;
    --rose-photo-b: #6d6b62;
    --portrait-a: #d9b59c;
    --portrait-b: #c49a88;
    --host-a: #efe6df;
    --host-b: #b9a89c;
  }
  * { margin: 0; padding: 0; box-sizing: border-box; }
  html, body { width: 1200px; height: 851px; overflow: hidden; background: #fff; }
  .flyer {
    position: relative; width: 1200px; height: 851px; overflow: hidden;
    background: radial-gradient(ellipse at 65% 50%, var(--lime-pale) 0%, var(--lime) 55%, var(--lime-deep) 100%);
    font-family: "Open Sans", sans-serif; color: var(--ink);
  }
  .header-panel {
    position: absolute; left: 0; top: 0; width: 1200px; height: 180px;
    background: var(--pink-header);
  }
  .header-roses {
    position: absolute; right: 0; top: 0; width: 520px; height: 180px;
    background: radial-gradient(ellipse at 70% 40%, rgba(240,150,170,0.55), rgba(247,192,216,0) 70%);
  }
  .shapes { position: absolute; inset: 0; }
  .title {
    position: absolute; left: 480px; top: 14px; width: 720px; text-align: center;
    font-family: "Great Vibes", cursive; font-size: 70px; font-weight: 400;
    -webkit-text-stroke: 1.2px var(--ink); letter-spacing: 1px; line-height: 1.1;
  }
  .sessions {
    position: absolute; left: 540px; top: 110px; width: 560px; text-align: center;
    font-weight: 700; font-size: 20px; line-height: 30px; list-style: none;
  }
  .venue-band {
    position: absolute; left: 440px; top: 186px; width: 760px; height: 40px;
    background: var(--band);
  }
  .venue {
    position: absolute; left: 470px; top: 188px; width: 710px;
    font-weight: 700; font-size: 24px; line-height: 36px; text-align: center;
  }
  .intro {
    position: absolute; left: 380px; top: 240px; width: 800px; text-align: center;
    font-family: "PT Sans Narrow", sans-serif; font-size: 25px; line-height: 33px; color: #2a2a2a;
  }
  .cost {
    position: absolute; left: 314px; top: 390px;
    color: var(--magenta); font-weight: 800; font-size: 30px; line-height: 34px;
  }
  .cost small { display: block; font-size: 22px; line-height: 28px; font-weight: 800; letter-spacing: 1px; }
  .materials { position: absolute; left: 314px; top: 466px; font-weight: 700; font-size: 23px; }
  .materials h2 { font-size: 23px; font-weight: 800; line-height: 32px; }
  .materials ul { list-style: none; }
  .materials li { line-height: 33px; display: flex; align-items: center; gap: 8px; }
  .materials li::before {
    content: ""; width: 22px; height: 22px; border-radius: 50%;
    background: radial-gradient(circle, #fff 0 18%, var(--magenta) 22%);
  }
  .photo-portrait {
    position: absolute; left: 0; top: 385px; width: 340px; height: 466px;
    background: linear-gradient(90deg, var(--portrait-b), var(--portrait-a) 60%, rgba(217,181,156,0) 100%);
  }
  .rose-spray {
    position: absolute; left: 440px; top: 500px; width: 300px; height: 150px; border-radius: 50%;
    background: radial-gradient(ellipse, rgba(240,150,170,0.7), rgba(240,150,170,0) 70%);
  }
  .rsvp-band {
    position: absolute; left: 300px; top: 690px; width: 600px; height: 132px;
    background: linear-gradient(90deg, rgba(200,170,140,0) 0%, var(--band-low) 25%, var(--band-low) 100%);
  }
  .rsvp {
    position: absolute; left: 320px; top: 692px; width: 570px; text-align: center;
    font-weight: 700; font-size: 28px; line-height: 40px;
  }
  .rsvp .email { font-size: 29px; }
  .rsvp .phone { font-size: 34px; font-weight: 800; letter-spacing: 1px; }
  .rsvp .phone em { font-size: 28px; font-weight: 700; letter-spacing: 0; }
  .rsvp svg { vertical-align: -3px; }
</style>
</head>
<body>
<main class="flyer">
  <div class="header-panel"><div class="header-roses" role="img" aria-label="Soft pink roses behind the title"></div></div>

  <div class="rose-spray" role="img" aria-label="Pink rose buds decoration"></div>

  <div class="photo-portrait" role="img" aria-label="Young woman wearing a floral crown of roses and berries"></div>

  <svg class="shapes" width="1200" height="851" viewBox="0 0 1200 851">
    <defs>
      <linearGradient id="rosesTone" x1="0" y1="0" x2="1" y2="1">
        <stop offset="0" stop-color="var(--rose-photo-b)"/>
        <stop offset="0.45" stop-color="var(--rose-photo-a)"/>
        <stop offset="1" stop-color="var(--rose-photo-b)"/>
      </linearGradient>
      <radialGradient id="hostTone" cx="0.45" cy="0.45" r="0.6">
        <stop offset="0" stop-color="var(--host-a)"/>
        <stop offset="1" stop-color="var(--host-b)"/>
      </radialGradient>
    </defs>
    <path role="img" aria-label="Peach roses and thistle buttonholes on a wooden table"
          d="M0 0 H486 C440 170 300 330 0 392 Z" fill="url(#rosesTone)"/>
    <path d="M486 0 C440 170 300 330 0 392" fill="none" stroke="var(--ring)" stroke-width="6"/>
    <path d="M0 400 C150 380 250 385 330 392" fill="none" stroke="var(--ring)" stroke-width="3" opacity="0.6"/>
    <circle role="img" aria-label="Florist Molly Brandt smiling in her flower studio"
            cx="1010" cy="655" r="265" fill="url(#hostTone)"/>
    <circle cx="1010" cy="655" r="268" fill="none" stroke="var(--ring)" stroke-width="7"/>
  </svg>

  <h1 class="title">Floral Crowns Workshop</h1>
  <ul class="sessions">
    <li>1: Saturday 11 April 2015, 11:00-2:00pm</li>
    <li>2: Thursday 23 April 2015, 6:00-9:00pm</li>
  </ul>

  <div class="venue-band"></div>
  <p class="venue">The Open Workroom, Unit 3, 17 Holloway Street Penrith</p>

  <p class="intro">Florist and lover of all things gorgeous, Molly Brandt from Molly Brandt Flowers<br>will be running this beautiful and fun workshop. Come along to learn how to make<br>your very own floral crown. All you need to bring are some closed in shoes,<br>an apron and an open mind ready for creativity!</p>

  <p class="cost">Cost: $90 per person<small>Teens &amp; adults welcome</small></p>

  <section class="materials">
    <h2>Materials provided:</h2>
    <ul>
      <li>Florist scissors</li>
      <li>Parafilm</li>
      <li>Wire</li>
      <li>Flowers</li>
      <li>light snacks &amp; refreshments</li>
    </ul>
  </section>

  <div class="rsvp-band"></div>
  <div class="rsvp">
    <p><em>RSVP to Molly via email</em></p>
    <p class="email">mollybrandtflowers@postvale.com</p>
    <p class="phone"><em>or call</em>
      <svg width="24" height="26" viewBox="0 0 24 26" aria-hidden="true"><path d="M6 2 L10 7 L7.5 10 C9 14 11 16.5 15 18.5 L18 16 L22 20 L19 24 C10 23 2 14 2 5 Z" fill="none" stroke="#1e1e1e" stroke-width="2"/></svg>
      0431.507.962</p>
  </div>
</main>
</body>
</html>
```